Supplement Bottle Packaging and Design

We want to rebrand our current health supplements (see below). We do want it to be modern, vibrant and appealing supplement bottles. Very upscale and elegant as it targets primarily women.
NOTE: READ THE ATTACHED WORD DOCUMENT!
Bottle size: We are totally open to the bottle size and shape, as long it's a typical supplement bottle size to handle 90-120 capsules; what we mostly need is new bottle design/packaging. YOU DON’T HAVE TO USE THE CURRENT WHITE BOTTLE SHAPE, BUT ANYTHING MORE MODERN WOULD WORK!
Updates
We need more modern, clean sleek designs to choose from
Look and feel
Each slider illustrates characteristics of the customer's brand and the style your logo design should communicate.

```html
<!DOCTYPE html>
<html lang="en">
<head>
<meta charset="utf-8">
<title>Poise Supplement Labels</title>
<link rel="stylesheet" href="https://fonts.googleapis.com/css2?family=Fira+Sans:wght@600;700&family=Ubuntu:wght@700&display=swap">
<style>
  :root {
    --stage: #a7a7a7;
    --white: #ffffff;

    --liver-light: #d2649c;
    --liver-mid: #c95a95;
    --liver-dark: #86366a;
    --liver-ink: #2a1822;

    --tummy-light: #d2272f;
    --tummy-dark: #1b1b1b;
    --tummy-ink: #2a1616;

    --hormone-light: #5a9f91;
    --hormone-dark: #2e5a50;
    --hormone-ink: #1d2b28;

    --sugar-light: #2c5fcb;
    --sugar-dark: #3b2e7e;
    --sugar-ink: #17163a;
  }
  * { box-sizing: border-box; margin: 0; padding: 0; }
  html, body { width: 1200px; height: 763px; overflow: hidden; }
  body {
    background: var(--stage);
    font-family: "Fira Sans", sans-serif;
    color: var(--white);
  }
  .label-row {
    position: absolute;
    top: 273px;
    left: 15px;
    display: flex;
    gap: 30px;
  }
  .label {
    position: relative;
    width: 270px;
    height: 216px;
    overflow: hidden;
  }
  .label-texture {
    position: absolute;
    inset: 0;
    background: linear-gradient(100deg, var(--light) 0%, var(--light) 35%, var(--dark) 100%);
  }
  .pill {
    position: absolute;
    display: flex;
    align-items: center;
    font-weight: 600;
    line-height: 1.2;
    white-space: nowrap;
  }
  .pill-title {
    left: 0; top: 0;
    width: 230px; height: 73px;
    border-radius: 0 36px 36px 0;
    background: var(--light);
    padding-left: 18px;
    font-family: "Ubuntu", sans-serif;
    font-weight: 700;
    font-size: 36px;
    letter-spacing: -0.2px;
  }
  .label-tummy .pill-title { font-size: 33px; padding-left: 11px; }
  .label-hormone .pill-title { font-size: 29px; padding-left: 12px; }
  .pill-title .accent { color: var(--ink); }
  .pill-title.stacked {
    flex-direction: column;
    align-items: flex-start;
    justify-content: center;
    font-size: 33px;
    line-height: 1.0;
    padding-left: 17px;
  }
  .pill-title.stacked .accent { align-self: flex-end; padding-right: 27px; }
  .pill-claim {
    left: 66px; top: 75px;
    width: 220px; height: 53px;
    border-radius: 27px 0 0 27px;
    background: var(--dark);
    padding-left: 24px;
    font-size: 15px;
  }
  .pill-type {
    left: 0; top: 130px;
    width: 231px; height: 39px;
    border-radius: 0 20px 20px 0;
    background: var(--light);
    padding-left: 50px;
    font-size: 15.5px;
  }
  .pill-count {
    left: 32px; top: 171px;
    width: 250px; height: 39px;
    border-radius: 20px 0 0 20px;
    background: var(--dark);
    padding-left: 17px;
    font-size: 15.5px;
  }
  .label-liver { --light: var(--liver-light); --dark: var(--liver-dark); --ink: var(--liver-ink); }
  .label-liver .pill-type { background: var(--liver-mid); }
  .label-tummy { --light: var(--tummy-light); --dark: var(--tummy-dark); --ink: var(--tummy-ink); }
  .label-hormone { --light: var(--hormone-light); --dark: var(--hormone-dark); --ink: var(--hormone-ink); }
  .label-sugar { --light: var(--sugar-light); --dark: var(--sugar-dark); --ink: var(--sugar-ink); }
</style>
</head>
<body>
  <main class="label-row">
    <section class="label label-liver">
      <div class="label-texture" role="img" aria-label="Faceted geometric pink texture"></div>
      <h2 class="pill pill-title">Liver&nbsp;<span class="accent">Poise</span></h2>
      <p class="pill pill-claim">Rejuvenating Cleanse<br>&amp; Detox Formula*</p>
      <p class="pill pill-type">Dietary Supplement</p>
      <p class="pill pill-count">120 Vegetable Capsules</p>
    </section>

    <section class="label label-tummy">
      <div class="label-texture" role="img" aria-label="Faceted geometric red and black texture"></div>
      <h2 class="pill pill-title">Tummy&nbsp;<span class="accent">Poise</span></h2>
      <p class="pill pill-claim">Oxygenating Colon<br>Cleanse*</p>
      <p class="pill pill-type">Dietary Supplement</p>
      <p class="pill pill-count">90 Vegetable Capsules</p>
    </section>

    <section class="label label-hormone">
      <div class="label-texture" role="img" aria-label="Faceted geometric teal texture"></div>
      <h2 class="pill pill-title">Hormone&nbsp;<span class="accent">Poise</span></h2>
      <p class="pill pill-claim">Supports Healthy<br>Hormone Levels*</p>
      <p class="pill pill-type">Dietary Supplement</p>
      <p class="pill pill-count">60 Vegetable Capsules</p>
    </section>

    <section class="label label-sugar">
      <div class="label-texture" role="img" aria-label="Faceted geometric blue and violet texture"></div>
      <h2 class="pill pill-title stacked"><span>Blood Sugar</span><span class="accent">Poise</span></h2>
      <p class="pill pill-claim">Supports Healthy<br>Blood Glucose Levels*</p>
      <p class="pill pill-type">Dietary Supplement</p>
      <p class="pill pill-count">60 Vegetable Capsules</p>
    </section>
  </main>
</body>
</html>
```